Complete collections of detective novels by Mathieu Delvarenne

Cover for a NUMERIC book: all the 11 detective novels by Mathieu Delvarenne.
Covers of these novels can be seen at https://www.editions-pavane.com/auteur/mathieu-delvarenne/ (but we don't want a patchwork).
All these books are connected with a medical atmosphere, they often include a beautiful women, some bandits and a detective.

Title: “The Casebook of Dr. M – The Complete 2024”
Author: “Mathieu Delvarenne”
Publisher: “Editions Pavane”

Target Market(s)

Readers of detective novels

Requirements
Must have
• Adapted to screen (it's a digital book)

```html
<!DOCTYPE html>
<html lang="en">
<head>
<meta charset="utf-8">
<title>The Casebook of Dr. M – The Complete 2024</title>
<link rel="stylesheet" href="https://fonts.googleapis.com/css2?family=Anton&family=Poppins:ital,wght@0,400;1,300&display=swap">
<style>
  :root {
    --page-bg: #c9dcdc;
    --teal-deep: #0b2e33;
    --teal-mid: #12606a;
    --teal-glow: #2aa9b5;
    --floor-dark: #0d1c1d;
    --ink-white: #f1f1ee;
    --blood-red: #d8262b;
    --accent-cyan: #1cc6c9;
  }
  * { margin: 0; padding: 0; box-sizing: border-box; }
  html, body {
    width: 1200px;
    height: 2400px;
    overflow: hidden;
    background: var(--page-bg);
  }
  .book-cover {
    position: absolute;
    left: 50px;
    top: 319px;
    width: 1100px;
    height: 1762px;
    overflow: hidden;
    box-shadow: 0 30px 60px rgba(20, 50, 55, 0.45);
    background: var(--teal-deep);
  }
  .cover-photo {
    position: absolute;
    inset: 0;
    background:
      radial-gradient(ellipse 22% 5% at 50% 9%, rgba(200, 255, 250, 0.55), transparent 70%),
      radial-gradient(ellipse 14% 30% at 50% 42%, rgba(170, 210, 210, 0.35), transparent 75%),
      radial-gradient(ellipse 70% 40% at 50% 30%, rgba(42, 169, 181, 0.55), transparent 75%),
      linear-gradient(90deg, #0a2226 0%, #16606b 18%, #0e3c43 40%, #0e3c43 60%, #16606b 82%, #0a2226 100%);
  }
  .cover-photo::after {
    content: "";
    position: absolute;
    inset: 0;
    background: linear-gradient(180deg, rgba(10, 40, 45, 0.2) 0%, transparent 35%, rgba(13, 28, 29, 0.6) 62%, var(--floor-dark) 100%);
  }
  .author-name {
    position: absolute;
    top: 262px;
    left: 0;
    width: 100%;
    text-align: center;
    font-family: "Anton", sans-serif;
    font-size: 78px;
    letter-spacing: 3px;
    color: var(--ink-white);
    line-height: 1;
    text-transform: uppercase;
  }
  .book-title {
    position: absolute;
    top: 1048px;
    left: 0;
    width: 100%;
    text-align: center;
    font-family: "Anton", sans-serif;
    color: var(--ink-white);
    text-transform: uppercase;
    line-height: 0.98;
    letter-spacing: -2px;
  }
  .book-title .line { display: block; }
  .book-title .line-the { font-size: 112px; }
  .book-title .line-main { font-size: 138px; }
  .book-title .line-doctor { font-size: 200px; margin-top: -6px; }
  .book-title .mark-red { color: var(--blood-red); }
  .edition-subtitle {
    position: absolute;
    top: 1490px;
    left: 0;
    width: 100%;
    text-align: center;
    font-family: "Poppins", sans-serif;
    font-style: italic;
    font-weight: 300;
    font-size: 56px;
    color: var(--accent-cyan);
    letter-spacing: 1px;
    text-transform: uppercase;
  }
  .publisher-name {
    position: absolute;
    top: 1650px;
    left: 0;
    width: 100%;
    text-align: center;
    font-family: "Poppins", sans-serif;
    font-weight: 400;
    font-size: 30px;
    letter-spacing: 0.3em;
    color: var(--ink-white);
    text-transform: uppercase;
  }
</style>
</head>
<body>
  <main class="book-cover">
    <div class="cover-photo" role="img" aria-label="Photograph of a long dim teal hospital corridor lit by ceiling lamps, a woman in a pale gown standing far down the hall"></div>
    <p class="author-name">Mathieu Delvarenne</p>
    <h1 class="book-title">
      <span class="line line-the">The</span>
      <span class="line line-main"><span class="mark-red">Case</span>book</span>
      <span class="line line-doctor"><span class="mark-red">Of</span> Dr. M</span>
    </h1>
    <p class="edition-subtitle">The Complete 2024</p>
    <p class="publisher-name">Editions Pavane</p>
  </main>
</body>
</html>
```